Holiday Rental Company Flyer Design (DL not A5)

Note from PixelFolk Administration: The category sizing selected is A5, however the project requires DL sized artwork. Please refer to the DL template link below while the 'Special Requirements' are updated accordingly.

Project Brief:
We need a double sided DL flyer designed for an up market Holiday Rental Company that portrays a personalised approach to property management. These are to be used for letter box drops to homes we're specifically targeting so the design should be modern, complimentary colour palette, uncluttered & visually appealing.

Please Download the DL Template from Quillmark here: http://www.quillmark.com.au/qm/ns/propath/UploadResources.aspx?selectedTab=0?pfid=BFB&pf_id=BFB&xnav=easypath-upload-image#Templates

Target Market(s)

Wealthy Home Owners

Industry/Entity Type

It Company

Font styles to use
Other font styles liked:
• Avant Garde Extra Light & Demi

Colors
33b8a4

Requirements
Must have
• DL Flyer sizes (210mm width x 99mm width, plus 3mm bleed)
• Front: Logo, Main Image & Grab
• Back: Contact Details & Brief Description of our business
• Images: Ideally the main image should be the house with the pool but alternatively a lifestyle images could also be used.
Nice to have
• A creative designer!
Should not have
• Clutter & busy designs

```html
<!DOCTYPE html>
<html lang="en">
<head>
<meta charset="utf-8">
<title>Harbourline Stays – DL Flyer</title>
<link rel="stylesheet" href="https://fonts.googleapis.com/css2?family=Questrial&family=Raleway:wght@200;300&display=swap">
<style>
  :root {
    --page: #ffffff;
    --brand-green: #3ff292;
    --brand-green-soft: #84f2bd;
    --mint-panel: #a6f7d0;
    --ink: #1f2a2a;
    --icon: #4a4f52;
    --white: #ffffff;
    --night-deep: #121d3a;
    --night-mid: #2b3f8a;
    --pool: #3fa0f0;
    --warm-light: #c9985a;
  }
  * { box-sizing: border-box; margin: 0; padding: 0; }
  html, body { width: 1122px; height: 1200px; overflow: hidden; background: var(--page); }
  .canvas { position: relative; width: 1122px; height: 1200px; }

  /* Front side */
  .flyer-front {
    position: absolute; left: 60px; top: 71px; width: 1002px; height: 487px; overflow: hidden;
  }
  .hero-photo {
    position: absolute; inset: 0;
    background:
      radial-gradient(ellipse 40% 45% at 22% 55%, rgba(201,152,90,0.85), rgba(201,152,90,0) 70%),
      linear-gradient(180deg, rgba(0,0,0,0) 65%, var(--pool) 82%, #5fc3ff 100%),
      linear-gradient(120deg, #1a1a22 0%, var(--night-deep) 35%, var(--night-mid) 70%, #6a78c9 100%);
  }
  .front-headline {
    position: absolute; left: 360px; top: 52px; width: 570px; text-align: center;
    font-family: "Raleway", sans-serif; font-weight: 200; font-size: 41px; line-height: 55px;
    color: var(--white);
  }
  .front-logo {
    position: absolute; left: 728px; top: 275px; width: 231px; height: 163px;
    background: var(--brand-green);
    display: flex; align-items: center; justify-content: center; text-align: center;
  }
  .logo-name {
    font-family: "Questrial", sans-serif; font-weight: 400; color: var(--white);
    text-transform: uppercase; letter-spacing: 0.14em; line-height: 1.2;
  }
  .front-logo .logo-name { font-size: 22px; }

  /* Back side */
  .flyer-back {
    position: absolute; left: 60px; top: 632px; width: 1002px; height: 488px; overflow: hidden;
  }
  .lifestyle-photo {
    position: absolute; left: 0; top: 0; width: 492px; height: 406px;
    background:
      linear-gradient(180deg, #c8cdd3 0%, #dfe3e6 40%, #b9dce6 55%, #8fc6d8 80%, #7fb8cc 100%);
  }
  .thumb { position: absolute; left: 51px; width: 151px; height: 101px; }
  .thumb-basin { top: 45px; background: linear-gradient(135deg, #c9ced0, #8e9a98); }
  .thumb-flowers { top: 165px; background: linear-gradient(135deg, #6b6f72, #c46a3a 70%, #e6a75a); }
  .thumb-bedroom { top: 281px; background: linear-gradient(135deg, #c8a984, #e8d27a 55%, #b44f6a); }

  .about-panel {
    position: absolute; left: 492px; top: 0; width: 510px; height: 406px;
    background: var(--mint-panel);
    padding: 20px 16px 0 15px;
    font-family: "Questrial", sans-serif; color: var(--ink);
  }
  .about-title {
    font-family: "Raleway", sans-serif; font-weight: 200; font-size: 36px; line-height: 42px;
    color: var(--white); margin-bottom: 10px;
  }
  .about-text { font-size: 14.2px; line-height: 17.5px; }
  .about-text p { margin-bottom: 17px; }
  .about-text ul { list-style: none; margin-top: 0; }
  .about-text li::before { content: "• "; }

  .back-logo {
    position: absolute; left: 18px; top: 294px; width: 136px; height: 95px;
    background: var(--brand-green-soft);
    display: flex; align-items: center; justify-content: center; text-align: center;
  }
  .back-logo .logo-name { font-size: 13px; }

  .contact-list { position: absolute; left: 183px; top: 292px; list-style: none; }
  .contact-list li {
    display: flex; align-items: center; gap: 9px; height: 26px; font-size: 14.5px;
  }
  .contact-list svg { width: 18px; height: 18px; flex: none; }

  .tagline-band {
    position: absolute; left: 0; top: 406px; width: 1002px; height: 82px;
    background: var(--brand-green);
    display: flex; align-items: center; justify-content: center;
    font-family: "Raleway", sans-serif; font-weight: 200; font-size: 35px; color: var(--white);
    letter-spacing: -0.02em;
  }
</style>
</head>
<body>
<main class="canvas">

  <section class="flyer-front">
    <div class="hero-photo" role="img" aria-label="Photograph of a modern luxury home at dusk with a lit swimming pool"></div>
    <h1 class="front-headline">Holiday Rental Management<br>with a difference</h1>
    <div class="front-logo"><span class="logo-name">Harbourline<br>Stays</span></div>
  </section>

  <section class="flyer-back">
    <div class="lifestyle-photo" role="img" aria-label="Photograph of a small sailing boat on calm bay water under a cloudy sky"></div>
    <div class="thumb thumb-basin" role="img" aria-label="Photograph of a bathroom basin and tap"></div>
    <div class="thumb thumb-flowers" role="img" aria-label="Photograph of flowers in a vase on a table"></div>
    <div class="thumb thumb-bedroom" role="img" aria-label="Photograph of a bed with yellow cushions and a patterned throw"></div>

    <div class="about-panel">
      <h2 class="about-title">What we do differently!</h2>
      <div class="about-text">
        <p>Rather than relying upon a key safe or a central pick-up destination, a ‘Harbourline Stays’ staff member will greet guests upon arrival.</p>
        <p style="margin-bottom:0">Our <strong>‘Meet &amp; Greet’</strong> service provides home owners with an increased level of Security and also allows us to:</p>
        <ul>
          <li>Prepare the home for their arrival (lights, heaters, music etc.)</li>
          <li>Establish a rapport &amp; help facilitate future bookings</li>
          <li>Reiterate their responsibilities to ensure the return of their bond</li>
        </ul>
        <p style="margin-top:17px">If you’d like to know what your property could achieve or require additional information, please contact us on:</p>
      </div>

      <div class="back-logo"><span class="logo-name">Harbourline<br>Stays</span></div>

      <ul class="contact-list">
        <li>
          <svg viewBox="0 0 18 18" aria-hidden="true"><circle cx="9" cy="9" r="9" fill="var(--icon)"/><path d="M6 4.5c.5-.3 1-.2 1.3.3l.8 1.5c.2.4.1.8-.2 1.1l-.6.5c.4 1 1.3 2 2.3 2.5l.5-.6c.3-.3.7-.4 1.1-.2l1.5.8c.5.3.6.8.3 1.3l-.5.8c-.4.6-1.2.8-1.9.5-2.4-1-4.3-2.9-5.2-5.3-.2-.7 0-1.4.6-1.8z" fill="var(--white)"/></svg>
          (03)5521 7730
        </li>
        <li>
          <svg viewBox="0 0 18 18" aria-hidden="true"><circle cx="9" cy="9" r="9" fill="var(--icon)"/><rect x="4.5" y="5.8" width="9" height="6.4" fill="none" stroke="var(--white)" stroke-width="1.2"/><path d="M4.5 6l4.5 3.4L13.5 6" fill="none" stroke="var(--white)" stroke-width="1.2"/></svg>
          stay@harbourlinestays.com.au
        </li>
        <li>
          <svg viewBox="0 0 18 18" aria-hidden="true"><circle cx="9" cy="9" r="9" fill="var(--icon)"/><rect x="4.5" y="5" width="9" height="6.5" fill="none" stroke="var(--white)" stroke-width="1.2"/><path d="M7 13.5h4M9 11.5v2" stroke="var(--white)" stroke-width="1.2"/></svg>
          harbourlinestays.com.au
        </li>
        <li>
          <svg viewBox="0 0 18 18" aria-hidden="true"><circle cx="9" cy="9" r="9" fill="var(--icon)"/><path d="M9 3.8a3.4 3.4 0 0 0-3.4 3.4c0 2.5 3.4 6.6 3.4 6.6s3.4-4.1 3.4-6.6A3.4 3.4 0 0 0 9 3.8z" fill="var(--white)"/><circle cx="9" cy="7.2" r="1.3" fill="var(--icon)"/></svg>
          PO Box 48, Sorrel Bay Victoria 3990
        </li>
      </ul>
    </div>

    <div class="tagline-band">It’s the way we put our service together that sets us apart</div>
  </section>

</main>
</body>
</html>
```